Invitation Design Project

I would like to have a custom invitation (and reception/response cards) designed for my son's Bar Mitzvah. I have a strong idea of what I want and have a few mock-ups, but my "home made" effort would be improved by the addition of professional creativity and skill. The invitation should be white, red, and black, and a bold typographic style (see attachment). I am looking for a clean modern feel, and prefer square shaped invitations. I need the final product in an electronic format that I could either print myself or have done at a local printer.

Target Market(s)

Guests to a Bar Mitzvah. A group of family and friends ranging from 40-60 years of age, and a group of my son's 13 year old friends.

Industry/Entity Type

Electronic

Requirements
Must have
• Square shaped invitation (exact dimensions in attached file)
Typographic style
Red, black, white
Red color should be CMYK: 30-96-76-26
Nice to have
• I like the two icons on my attached sample reception card, especially the swirl/Torah one. I would be nice to use these (or similar ones) if there is a way to do so, but this is not a requirement.

```html
<!DOCTYPE html>
<html lang="en">
<head>
<meta charset="utf-8">
<title>Reception Card</title>
<link rel="stylesheet" href="https://fonts.googleapis.com/css2?family=Bebas+Neue&family=Jost:wght@500;600&display=swap">
<style>
  :root {
    --red: #cf373a;
    --ink: #2a2a2a;
    --band: #242424;
    --paper: #ffffff;
    --shade: #9c9c9c;
    --fold: #bdbdbd;
  }
  html, body {
    margin: 0;
    padding: 0;
    width: 1200px;
    height: 1200px;
    overflow: hidden;
  }
  .card-canvas {
    position: relative;
    width: 1200px;
    height: 1200px;
    background: var(--red);
    overflow: hidden;
  }
  .card-shadow {
    position: absolute;
    left: 130px;
    top: 130px;
    width: 968px;
    height: 968px;
    background: var(--band);
  }
  .card-sheet {
    position: absolute;
    left: 118px;
    top: 118px;
    width: 968px;
    height: 968px;
    background: var(--paper);
  }
  .band-folds {
    position: absolute;
    left: 0;
    top: 0;
    width: 1200px;
    height: 1200px;
  }
  .title-band {
    position: absolute;
    left: 72px;
    top: 177px;
    width: 1059px;
    height: 300px;
    background: var(--band);
    display: flex;
    align-items: center;
    justify-content: center;
  }
  .title-band h1 {
    margin: 0;
    padding-left: 0.28em;
    font-family: "Bebas Neue", "Oswald", sans-serif;
    font-weight: 400;
    font-size: 146px;
    letter-spacing: 0.28em;
    color: var(--paper);
    line-height: 1;
  }
  .details {
    position: absolute;
    left: 0;
    top: 0;
    width: 1200px;
    height: 1200px;
    font-family: "Jost", "Futura", sans-serif;
    color: var(--ink);
    text-shadow: 4px 4px 0 var(--shade);
  }
  .details p {
    position: absolute;
    left: 165px;
    width: 881px;
    margin: 0;
    line-height: 1;
    white-space: nowrap;
    text-align: justify;
    text-align-last: justify;
  }
  .invite-line {
    top: 509px;
    font-size: 114px;
    font-weight: 600;
    text-align: left !important;
    text-align-last: left !important;
  }
  .occasion-line {
    top: 633px;
    font-size: 54px;
    font-weight: 500;
    letter-spacing: 15px;
    margin-right: -15px !important;
    width: 896px !important;
  }
  .occasion-line.tight {
    top: 696px;
    letter-spacing: 2px;
    margin-right: 0 !important;
    width: 881px !important;
  }
  .time-line {
    top: 746px;
    font-size: 145px;
    font-weight: 500;
    letter-spacing: 2px;
  }
  .venue-line {
    top: 891px;
    font-size: 104px;
    font-weight: 500;
    letter-spacing: 5px;
  }
  .address-line {
    top: 993px;
    font-size: 42px;
    font-weight: 600;
    text-shadow: 3px 3px 0 var(--shade);
  }
</style>
</head>
<body>
  <main class="card-canvas">
    <div class="card-shadow"></div>
    <div class="card-sheet"></div>
    <svg class="band-folds" viewBox="0 0 1200 1200" aria-hidden="true">
      <polygon points="72,477 118,477 118,500" fill="var(--fold)"/>
      <polygon points="1086,477 1131,477 1086,500" fill="var(--fold)"/>
    </svg>
    <header class="title-band">
      <h1>Reception</h1>
    </header>
    <section class="details">
      <p class="invite-line">PLEASE JOIN US</p>
      <p class="occasion-line">for lunch, dancing and</p>
      <p class="occasion-line tight">celebration following the service</p>
      <p class="time-line">1:00-4:30PM</p>
      <p class="venue-line">The Old Mill Hall</p>
      <p class="address-line">2250 Birch Hollow Road, Fairview, VA 22199</p>
    </section>
  </main>
</body>
</html>
```